Lead Sales Portal Needs to Generate B2B Signup's

We are looking for banner ad designs to drive new business (B2B) traffic to our insurance and mortgage industry self serve lead sites. The sites are HomeLoanProspectHub.com and PolicyProspectHub.com, and we service over 45,000 insurance agents and mortgage lenders in a self serve lead portal model. We want our banners to generate more of these clients.

Our clients come to our sites, browse our database and then pick out and purchase the consumer leads that they need to generate new business.

We advertise extensively on Zorvex and on other PPC platforms, and our existing banners are looking really tired.

Some of the ad copy that works well for us is:

Cherry Pick Your Life Leads - Why Pay More Than $3.50 For Life Insurance Leads?
Sign up today and we'll match up to $250

Agents - Here's $250 For New Clients. Cherry Pick Your Life Insurance Leads & Save! Sign up today and we'll match up to $250

One of our Landing Pages that performs well is here:
http://www.policyprospecthub.com/lp/008/

One of our competitors ad's are here:

http://www.brivlo.com/search/results?q=QuipRate&ad=427360

We're looking for a design that is eye catching, uses our "Deeply Discounted Leads" and our "$250 match bonus"

Target Market(s)

These are insurance agents and mortgage lenders. All of our clients are business' or individuals within the business. This is a B2B campaign,

Industry/Entity Type

Insurance

Requirements
Must have
• We must have the logos for the sites in the banners. Also, we must have a call to action arrow and "Go" button

One or two designs.

File type

.JPEG
.JPG
.PNG
.GIF

File size

150 KB or smaller

Image sizes

Vertical rectangle: 240 x 400
Mobile leaderboard: 320 x 50
Banner: 468 x 60
Leaderboard: 728 x 90
Square: 250 x 250
Small square: 200 x 200
Large rectangle: 336 x 280
Inline rectangle: 300 x 250
Skyscraper: 120 x 600
Wide skyscraper: 160 x 600
Half-page: 300 x 600
Large leaderboard: 970 x 90

```html
<!DOCTYPE html>
<html lang="en">
<head>
<meta charset="utf-8">
<title>Policy Prospect Hub – Banner Set</title>
<link rel="stylesheet" href="https://fonts.googleapis.com/css2?family=Josefin+Sans:wght@600;700&family=Lato:wght@700;900&display=swap">
<style>
:root{
  --bg:#e9e4dc;
  --green:#8cc63f;
  --yellow:#f9d423;
  --white:#ffffff;
  --orange:#f15a22;
  --ink:#1e1e1e;
  --photo-a:#5f6f4a;
  --photo-b:#2a2a2a;
}
*{margin:0;padding:0;box-sizing:border-box}
html,body{width:1200px;height:1002px;overflow:hidden;background:var(--bg)}
.stage{position:relative;width:1004px;height:838px;transform:scale(1.1952);transform-origin:0 0}
.banner{position:absolute;background:var(--green);overflow:hidden;font-family:"Josefin Sans",sans-serif;box-shadow:0 2px 6px rgba(0,0,0,.25)}
.brand{display:flex;align-items:center;gap:6px;background:var(--white);color:var(--ink);font-family:"Josefin Sans",sans-serif;font-weight:600;white-space:nowrap}
.brand-dot{border-radius:50%;background:var(--ink);flex:none}
.headline{color:var(--yellow);font-weight:700;line-height:1.05;white-space:nowrap;position:relative;z-index:2}
.copy{color:var(--white);font-weight:700;line-height:1.1;position:relative;z-index:2}
.cta{position:absolute;z-index:3;display:flex;align-items:center;justify-content:center;background:var(--orange);color:var(--white);font-family:"Lato",sans-serif;font-weight:900;border-radius:4px;letter-spacing:-.5px}
.photo{position:absolute;z-index:1;background:linear-gradient(160deg,var(--photo-a),var(--photo-b))}
.arrow{position:absolute;z-index:2}

/* leaderboard 728x90 */
.leaderboard{left:123px;top:48px;width:728px;height:90px}
.leaderboard .brand{position:absolute;left:0;top:0;width:138px;height:90px;justify-content:center;font-size:13px;flex-direction:column;gap:4px}
.leaderboard .brand-dot{width:28px;height:28px}
.leaderboard .headline{position:absolute;left:146px;top:11px;font-size:16.5px}
.leaderboard .copy{position:absolute;left:146px;top:33px;font-size:20px}
.leaderboard .cta{left:527px;top:35px;width:91px;height:24px;font-size:16px}
.leaderboard .photo{left:622px;top:0;width:106px;height:90px}
.leaderboard .arrow{left:462px;top:56px}

/* skyscraper 160x600 */
.skyscraper{left:123px;top:181px;width:160px;height:600px}
.skyscraper .brand{height:62px;padding-left:4px;gap:4px;font-size:12px;border-bottom:2px solid var(--orange)}
.skyscraper .brand-dot{width:26px;height:26px}
.skyscraper .notch{position:absolute;left:20px;top:62px}
.skyscraper .headline{position:absolute;left:0;top:103px;width:160px;text-align:center;font-size:22px;white-space:normal}
.skyscraper .copy{position:absolute;left:0;top:216px;width:160px;text-align:center;font-size:19px}
.skyscraper .arrow{left:128px;top:322px}
.skyscraper .cta{left:15px;top:383px;width:136px;height:37px;font-size:26px}
.skyscraper .photo{left:0;top:440px;width:160px;height:160px}

/* rectangle 300x250 */
.rectangle{left:337px;top:181px;width:300px;height:250px}
.rectangle .brand{height:44px;padding-left:54px;font-size:19px;border-bottom:2px solid var(--orange)}
.rectangle .brand-dot{width:38px;height:38px;position:absolute;left:54px;top:3px}
.rectangle .brand-name{margin-left:44px}
.rectangle .notch{position:absolute;left:26px;top:44px}
.rectangle .headline{position:absolute;left:0;top:58px;width:300px;text-align:center;font-size:22px}
.rectangle .copy{position:absolute;left:8px;top:117px;width:160px;font-size:14.5px;line-height:1.2}
.rectangle .arrow{left:84px;top:178px}
.rectangle .cta{left:12px;top:219px;width:90px;height:24px;font-size:17px}
.rectangle .photo{left:160px;top:104px;width:140px;height:146px}
</style>
</head>
<body>
<main class="stage">

  <section class="banner leaderboard" aria-label="Leaderboard banner">
    <div class="brand"><span class="brand-dot"></span><span>Policy Prospect Hub</span></div>
    <p class="headline">Why Pay More Than $3.50For Life Insurance Leads?</p>
    <p class="copy">Receive $250 Worth of Life Insurance<br>Leads Today by Just Signing Up</p>
    <svg class="arrow" width="66" height="22" viewBox="0 0 66 22"><path d="M2 16 Q30 24 62 6" fill="none" stroke="var(--orange)" stroke-width="2"/><path d="M52 4 L63 5 L58 14" fill="none" stroke="var(--orange)" stroke-width="2"/></svg>
    <div class="cta">SIGN UP</div>
    <div class="photo" role="img" aria-label="Photo of two smiling young business professionals in suits"></div>
  </section>

  <section class="banner skyscraper" aria-label="Skyscraper banner">
    <div class="brand"><span class="brand-dot"></span><span>Policy Prospect Hub</span></div>
    <svg class="notch" width="12" height="8" viewBox="0 0 12 8"><path d="M0 0 H12 L6 8Z" fill="var(--orange)"/></svg>
    <p class="headline">Why Pay More<br>Than $3.50 For<br>Life Insurance<br>Leads?</p>
    <p class="copy">Receive $250<br>Worth of Life<br>Insurance Leads<br>Today by Just<br>Signing Up</p>
    <svg class="arrow" width="30" height="52" viewBox="0 0 30 52"><path d="M6 2 Q28 20 14 48" fill="none" stroke="var(--orange)" stroke-width="2"/><path d="M8 38 L14 49 L24 42" fill="none" stroke="var(--orange)" stroke-width="2"/></svg>
    <div class="cta">SIGN UP</div>
    <div class="photo" role="img" aria-label="Photo of two smiling young business professionals in suits"></div>
  </section>

  <section class="banner rectangle" aria-label="Rectangle banner">
    <div class="brand"><span class="brand-dot"></span><span class="brand-name">Policy Prospect Hub</span></div>
    <svg class="notch" width="12" height="8" viewBox="0 0 12 8"><path d="M0 0 H12 L6 8Z" fill="var(--orange)"/></svg>
    <p class="headline">Why Pay More Than $3.50<br>For Life Insurance Leads?</p>
    <div class="photo" role="img" aria-label="Photo of two smiling young business professionals in suits"></div>
    <p class="copy">Receive $250 Worth<br>of Life Insurance<br>Leads Today by Just<br>Signing Up</p>
    <svg class="arrow" width="38" height="40" viewBox="0 0 38 40"><path d="M4 2 Q30 8 20 36" fill="none" stroke="var(--orange)" stroke-width="2"/><path d="M12 28 L20 37 L30 30" fill="none" stroke="var(--orange)" stroke-width="2"/></svg>
    <div class="cta">SIGN UP</div>
  </section>

</main>
</body>
</html>
```